Judicial election website to attract voters

I need a simple one-page web design for a judicial election. I'm going to put up one picture, maybe two. The picture I have needs a little touch-up (whiten teeth for example). I have 3 paragraphs of text. I'd like a "Donate" button that can link to a CoinDrift account. I'd also like a little background design, like the Constitution or something like that. There's a couple other little things but that's the bulk of it.

Target Market(s)

Involved voters and some media

Industry/Entity Type

Legal

Number of Pages Required

1 page

Font styles to use
Sans Serif

Requirements
Must have
• My picture, text, donate button
• Phrase "Remember to vote August 30, 2016!"
Nice to have
• Perhaps a second photo, maybe a short 30 second video of me talking directly to the voters, cool background: Constitution, something judgey.
Should not have
• Not sure ... profanity, I guess.

```html
<!DOCTYPE html>
<html lang="en">
<head>
<meta charset="utf-8">
<title>Remember to Vote – Judicial Election</title>
<link href="https://fonts.googleapis.com/css2?family=Open+Sans:wght@400;600;700&family=Great+Vibes&display=swap" rel="stylesheet">
<style>
:root{
  --red:#c8202f;
  --red-dark:#a81824;
  --navy:#142039;
  --navy-2:#1d2c4d;
  --ink:#2b2b2b;
  --text:#5d5d5d;
  --muted:#9a9a9a;
  --line:#e4e4e4;
  --band:#ececec;
  --panel:#f4f4f4;
  --footer:#333333;
  --footer-deep:#2a2a2a;
  --footer-text:#bdbdbd;
}
*{box-sizing:border-box;margin:0;padding:0}
html,body{width:1200px;height:2230px;overflow:hidden}
body{font-family:"Open Sans",Arial,sans-serif;color:var(--text);background:#fff;position:relative;font-size:10px;line-height:1.55}
.abs{position:absolute}
.wrap{position:absolute;left:259px;width:693px}
.section-title{font-size:12px;font-weight:600;color:var(--ink);text-transform:uppercase;letter-spacing:.2px}

/* header & hero */
.hero{position:absolute;left:0;top:0;width:1200px;height:378px;background:radial-gradient(ellipse at 50% 45%,#24355a 0%,#18264a 45%,#101a33 100%)}
.hero-map{position:absolute;left:160px;top:40px;width:900px;height:320px;border-radius:40%;background:radial-gradient(ellipse at 40% 50%,rgba(255,255,255,.06),rgba(255,255,255,0) 70%)}
.logo{position:absolute;left:259px;top:0;width:187px;height:73px;background:#e9e9e9;display:flex;align-items:center;justify-content:center;font-family:"Great Vibes",cursive;font-size:34px;color:#333}
.topbar{position:absolute;right:248px;top:6px;display:flex;align-items:center;gap:7px;font-size:8px;color:#b9c2d6}
.topbar .dot{width:10px;height:10px;border-radius:50%;background:#2f9fd8}
.topbar .sq{width:9px;height:8px;border:1px solid #b9c2d6;border-radius:1px}
.nav{position:absolute;left:453px;top:20px;height:53px;display:flex;align-items:center}
.nav a{font-size:8.5px;font-weight:600;color:#fff;text-decoration:none;text-transform:uppercase;padding:0 23px;height:53px;display:flex;align-items:center}
.nav a.active{background:rgba(255,255,255,.05);border-top:2px solid var(--navy-2);padding:0 24px}
.nav a.donate{background:var(--red);height:22px;padding:0 10px;margin-left:8px;border-radius:1px}
.nav-rule{position:absolute;left:453px;top:20px;width:499px;height:1px;background:rgba(255,255,255,.12)}
.home-tab{position:absolute;left:453px;top:73px;width:70px;height:42px}
.hero-points{position:absolute;left:272px;top:168px;list-style:none}
.hero-points li{display:flex;align-items:center;gap:12px;height:44px;font-size:20px;color:#fff}
.hero-points .ic{width:25px;height:25px;border-radius:50%;background:var(--red);display:flex;align-items:center;justify-content:center}
.hero-photo{position:absolute;left:699px;top:104px;width:232px;height:274px;background:linear-gradient(160deg,#2d56c4 0%,#1c3fa8 55%,#1a2c63 100%);transform:skewX(-2deg)}
.slider-dots{position:absolute;left:593px;top:355px;display:flex;gap:4px}
.slider-dots span{width:9px;height:9px;border-radius:50%;border:1.5px solid #fff}
.slider-dots span.on{background:#fff}

/* tagline band */
.tagline{position:absolute;left:0;top:378px;width:1200px;height:80px;background:var(--band);text-align:center}
.tagline h2{font-weight:400;font-size:17px;color:#444;margin-top:21px}
.tagline h2 em{font-style:normal;color:var(--red)}
.tagline p{font-size:9.5px;color:var(--muted);margin-top:1px}
.tagline-arrow{position:absolute;left:590px;top:458px;width:0;height:0;border-left:16px solid transparent;border-right:16px solid transparent;border-top:16px solid var(--band)}

/* global issues */
.tabs-v{position:absolute;left:259px;top:538px;width:159px}
.tabs-v div{height:30px;margin-bottom:3px;background:#eaeaea;font-size:9.5px;color:#555;text-transform:uppercase;padding-left:10px;display:flex;align-items:center}
.tabs-v div.on{background:var(--red);color:#fff}
.issue-panel{position:absolute;left:422px;top:538px;width:290px;height:250px;border:1px solid var(--line);padding:17px 12px 0}
.issue-photo{float:left;width:113px;height:112px;margin-right:13px;background:linear-gradient(180deg,#b9a585,#8d7a63)}
.issue-panel h3{font-size:11px;font-weight:600;color:var(--ink);line-height:1.4;margin-bottom:6px}
.issue-panel p{font-size:8.8px;line-height:1.6;margin-bottom:8px}
.events{position:absolute;left:732px;top:510px;width:220px}
.event{display:flex;gap:12px;height:83px;margin-top:0}
.event .date{width:32px;flex:none}
.event .date .d{height:37px;background:#ececec;text-align:center;font-size:13px;color:#444;line-height:1;padding-top:7px}
.event .date .d small{display:block;font-size:7px;text-transform:uppercase;margin-top:2px}
.event .date .y{height:14px;background:var(--red);color:#fff;font-size:7px;text-align:center;line-height:14px}
.event h4{font-size:10px;font-weight:400;color:var(--ink);margin-top:3px}
.event p{font-size:8.6px;line-height:1.55;margin-top:2px}
.event .meta{font-size:7.3px;color:#888;margin-top:6px;display:flex;gap:14px;align-items:center}
.meta i{display:inline-block;width:7px;height:7px;border:1px solid #999;border-radius:50%;margin-right:4px;vertical-align:-1px}

/* news */
.news{position:absolute;left:259px;top:849px;display:flex;gap:14px}
.news-card{width:221px;height:265px;border:1px solid #ededed;text-align:center}
.news-card .img{height:149px}
.news-card h3{font-size:10.5px;font-weight:400;color:var(--ink);margin-top:11px}
.news-card .meta{font-size:7.3px;color:#888;margin-top:3px;padding-bottom:9px;border-bottom:1px solid #ededed}
.news-card .meta span{margin:0 6px}
.news-card p{font-size:8.6px;line-height:1.55;padding:9px 16px 0}
.news-card a{display:block;font-size:8.3px;color:var(--red);text-decoration:none;margin-top:7px}

/* team */
.team-band{position:absolute;left:0;top:1176px;width:1200px;height:384px;background:linear-gradient(90deg,#e4e4e4,#ededed 25%,#e2e2e2 50%,#efefef 75%,#e3e3e3)}
.team{position:absolute;left:259px;top:1236px;display:flex;gap:18px}
.member{width:159px;height:291px;background:#fff;text-align:center}
.member .img{height:159px;border-bottom:2px solid var(--red)}
.member h3{font-size:11px;font-weight:400;color:var(--ink);margin-top:8px}
.member .role{font-size:7.8px;color:var(--muted);padding-bottom:8px;border-bottom:1px solid #eee;margin:0 8px}
.member p{font-size:8.6px;line-height:1.55;padding:8px 12px 0}
.member .socials{display:flex;gap:3px;justify-content:center;margin-top:10px}
.member .socials span{width:11px;height:11px;background:#9a9a9a;border-radius:2px}

/* facts & involved */
.accordion{position:absolute;left:259px;top:1621px;width:337px}
.acc-head{height:30px;background:var(--red);color:#fff;font-size:10px;font-weight:600;display:flex;align-items:center;padding:0 12px;gap:14px;position:relative}
.acc-head .tog{position:absolute;right:10px;width:8px;height:8px;border:1px solid rgba(255,255,255,.7)}
.acc-body{padding:13px 12px 20px;font-size:8.6px;line-height:1.6}
.acc-body p+p{margin-top:6px}
.acc-body b{color:var(--ink);font-weight:600}
.acc-item{height:30px;background:#e8e8e8;margin-bottom:4px;font-size:9.5px;color:#555;display:flex;align-items:center;padding-left:40px;position:relative}
.acc-item .ic{position:absolute;left:12px;width:10px;height:10px;background:#aaa;border-radius:2px}
.acc-item .tog{position:absolute;right:10px;width:8px;height:8px;border:1px solid #aaa}
.tabs-h{position:absolute;left:614px;top:1621px;display:flex;gap:5px}
.tabs-h div{height:30px;padding:0 12px;background:#e8e8e8;font-size:9.5px;color:#555;display:flex;align-items:center}
.tabs-h div.on{background:var(--red);color:#fff;font-weight:600}
.involved{position:absolute;left:614px;top:1653px;width:337px;height:203px;border:1px solid var(--line);padding:13px 13px 0}
.involved .img{height:94px;background:linear-gradient(180deg,#7fa4d2 0%,#a9c3e3 55%,#8a8f86 100%)}
.involved h4{font-size:8.8px;font-weight:600;color:#444;margin-top:15px}
.involved p{font-size:8.6px;line-height:1.6;margin-top:6px}

/* social band & footer */
.social-band{position:absolute;left:0;top:1905px;width:1200px;height:68px;background:linear-gradient(90deg,#1b1f28,#3a3f48 30%,#262a33 55%,#45464a 80%,#1d2028)}
.social-band .row{position:absolute;left:508px;top:1926px;display:flex;gap:10px}
.soc{width:24px;height:24px;border-radius:50%}
footer{position:absolute;left:0;top:1973px;width:1200px;height:198px;background:var(--footer)}
.fcol{position:absolute;top:2007px}
.fcol h5{font-size:8.5px;font-weight:600;color:#fff;text-transform:uppercase;margin-bottom:14px}
.fnews li{list-style:none;display:flex;gap:9px;height:42px}
.fnews .th{width:30px;height:30px;flex:none}
.fnews b{display:block;font-size:8.6px;font-weight:400;color:#fff;line-height:1.3}
.fnews small{font-size:7px;color:#8d8d8d}
.tags{display:flex;flex-wrap:wrap;gap:3px;width:150px}
.tags span{font-size:7px;color:#ddd;border:1px solid #555;padding:2px 7px}
.fcontact p{font-size:8.4px;color:#eee;line-height:1.55;width:160px}
.fcontact ul{list-style:none;margin-top:20px}
.fcontact li{font-size:8.2px;color:#eee;display:flex;gap:9px;margin-bottom:8px;line-height:1.35}
.fcontact li i{width:7px;height:7px;flex:none;background:#ddd;border-radius:50%;margin-top:3px}
.gallery{display:grid;grid-template-columns:repeat(4,34px);gap:3px;margin-top:-2px}
.gallery span{height:34px}
.bottombar{position:absolute;left:0;top:2171px;width:1200px;height:59px;background:var(--footer-deep)}
.copyright{position:absolute;left:259px;top:2183px;height:28px;border-left:1px solid #555;padding-left:11px;display:flex;align-items:center;font-size:7.8px;color:#ddd}
.flinks{position:absolute;right:248px;top:2183px;height:28px;display:flex;gap:14px;align-items:center;font-size:7.8px;color:#ddd;border-right:1px solid #555;padding-right:11px}
.flinks i{display:inline-block;width:7px;height:7px;background:#ddd;margin-right:4px;vertical-align:-1px}
</style>
</head>
<body>

<header class="hero">
  <div class="hero-map" role="img" aria-label="Faint world map across the dark blue background"></div>
  <div class="logo">Logo Here</div>
  <div class="topbar">
    <span>Call: 555-014-2270</span>
    <span class="dot"></span><span class="dot"></span><span class="dot"></span>
    <span class="sq"></span>
    <svg width="9" height="9" viewBox="0 0 10 10"><circle cx="4" cy="4" r="3" fill="none" stroke="#b9c2d6" stroke-width="1.3"/><line x1="6.3" y1="6.3" x2="9" y2="9" stroke="#b9c2d6" stroke-width="1.3"/></svg>
  </div>
  <div class="nav-rule"></div>
  <nav class="nav">
    <a class="active" href="#">Home</a>
    <a href="#">Pages</a>
    <a href="#">Gallery</a>
    <a href="#">Shortcodes</a>
    <a href="#">Shop</a>
    <a class="donate" href="#">Donate</a>
  </nav>
  <svg class="home-tab" viewBox="0 0 70 42"><path d="M0 0H70V28L35 42L0 28Z" fill="#1f3160"/><path d="M28 22L35 15L42 22M30 21V28H40V21" fill="none" stroke="#fff" stroke-width="2"/></svg>

  <ul class="hero-points">
    <li><span class="ic"><svg width="12" height="12" viewBox="0 0 12 12"><path d="M2 6.5L5 9L10 3" fill="none" stroke="#fff" stroke-width="2"/></svg></span>Country Needs a Change</li>
    <li><span class="ic" style="color:#fff;font-size:14px;font-weight:700">$</span>Prosperity and Progress</li>
    <li><span class="ic"><svg width="13" height="13" viewBox="0 0 12 12"><path d="M6 1L7.4 4.3L11 4.6L8.3 7L9.1 10.5L6 8.7L2.9 10.5L3.7 7L1 4.6L4.6 4.3Z" fill="#fff"/></svg></span>Great Plans for Great People</li>
  </ul>
  <div class="hero-photo" role="img" aria-label="Hand holding up a blue protest sign about marching and voting"></div>
  <div class="slider-dots"><span></span><span class="on"></span></div>
</header>

<section class="tagline">
  <h2>Every <em>Election</em> is Determined by the People Who <em>Show Up</em></h2>
  <p>Remember to vote August 30, 2016 – every single voice counts this year</p>
</section>
<div class="tagline-arrow"></div>

<h2 class="section-title abs" style="left:259px;top:508px">Global Issues</h2>
<div class="tabs-v">
  <div class="on">Experienced</div>
  <div>Dedicated</div>
  <div>Respected</div>
</div>
<article class="issue-panel">
  <div class="issue-photo" role="img" aria-label="Portrait photo of the candidate"></div>
  <h3>Political acdiam pharetra mattis neselinw</h3>
  <p>Nationsla seam ac diam pharetra mattis ut eget elit. Vestib ulum inerse pharetra dolor. Aliquam ultrice rutrum libero ut pulv inar lectus tincidunt inbe. Nunc nibh eliter feugiat sed congue.</p>
  <p style="clear:both">consce ctetur none.Donec sed odio dui. Nulla vitae elit libero, a pharetra augue. Nullam id dolor id nibh ultricies vehicula ut id elit. Integer posuere erat a ante venenatis dapibus posuere velit aliquet.</p>
  <p>Donec sed odio dui. Nulla vitae elit libero, a pharetra augue. Nullam id dolor id nibh ultricies vehicula ut id elit. Integer posuere erat velit aliquet.</p>
</article>

<h2 class="section-title abs" style="left:732px;top:508px">Upcoming Events</h2>
<div class="events" style="top:541px">
  <div class="event"><div class="date"><div class="d">14<small>Sep</small></div><div class="y">2016</div></div>
    <div><h4>Integer odio ultrici</h4><p>Nulla tempus neque massa, id mollis neque convallis ut. Morbi est velit, tincidunt</p><div class="meta"><span><i></i>Wednesday - 8:00 am</span><span><i></i>Cross Road Park</span></div></div></div>
  <div class="event"><div class="date"><div class="d">28<small>Sep</small></div><div class="y">2016</div></div>
    <div><h4>Supendie vitae lectus dict</h4><p>Nulla tempus neque massa, id mollis neque convallis ut. Morbi est velit, tincidunt</p><div class="meta"><span><i></i>Wednesday - 8:00 am</span><span><i></i>Cross Road Park</span></div></div></div>
  <div class="event"><div class="date"><div class="d">19<small>Oct</small></div><div class="y">2016</div></div>
    <div><h4>Nunc sit amet erat sollici</h4><p>Nulla tempus neque massa, id mollis neque convallis ut. Morbi est velit, tincidunt</p><div class="meta"><span><i></i>Wednesday - 8:00 am</span><span><i></i>Cross Road Park</span></div></div></div>
</div>

<h2 class="section-title abs" style="left:259px;top:820px">Latest News</h2>
<div class="news">
  <article class="news-card"><div class="img" role="img" aria-label="Group of young people in a circle seen from below" style="background:linear-gradient(180deg,#8fc3ea,#e9b44b 60%,#c98a3a)"></div>
    <h3>Platform of the political party</h3><div class="meta"><span><i></i>27 May, 2014</span><span><i></i>4 Comments</span></div>
    <p>Polint stdunt dolor sit amet constetur adipisicing elit sed do eiusmod tempor incididuabore et</p><a href="#">Read more ›</a></article>
  <article class="news-card"><div class="img" role="img" aria-label="Smiling group of friends in front of a flag" style="background:linear-gradient(180deg,#c9404c 0%,#e9e2e2 40%,#8f9ed1 100%)"></div>
    <h3>Don't believe the headlines</h3><div class="meta"><span><i></i>25 May, 2014</span><span><i></i>0 Comments</span></div>
    <p>Polint stdunt dolor sit amet constetur adipisicing elit sed do eiusmod tempor incididuabore et</p><a href="#">Read more ›</a></article>
  <article class="news-card"><div class="img" role="img" aria-label="Capitol building at sunset" style="background:linear-gradient(180deg,#2c4f86 0%,#5c79a8 50%,#e09a4a 80%,#2c2a35 100%)"></div>
    <h3>Restoring America's standing</h3><div class="meta"><span><i></i>23 May, 2014</span><span><i></i>0 Comments</span></div>
    <p>Polint stdunt dolor sit amet constetur adipisicing elit sed do eiusmod tempor incididuabore et</p><a href="#">Read more ›</a></article>
</div>

<div class="team-band" role="img" aria-label="Pale grey wood texture background"></div>
<h2 class="section-title abs" style="left:259px;top:1204px">Leadership Team</h2>
<div class="team">
  <div class="member"><div class="img" role="img" aria-label="Portrait of team member" style="background:linear-gradient(180deg,#9a9a9a,#cfcac4)"></div><h3>Laura Pennick</h3><div class="role">Project Manager</div><p>Lorem ipsum dolor sit ameteprenim consetetur sadipscing elitr sedes diam nonumy eirmod tempor.</p><div class="socials"><span></span><span></span><span></span><span></span></div></div>
  <div class="member"><div class="img" role="img" aria-label="Portrait of team member" style="background:linear-gradient(180deg,#a2a2a2,#c9bfb6)"></div><h3>Mara Quill</h3><div class="role">Policy Analyst</div><p>Lorem ipsum dolor sit ameteprenim consetetur sadipscing elitr sedes diam nonumy eirmod tempor.</p><div class="socials"><span></span><span></span><span></span><span></span></div></div>
  <div class="member"><div class="img" role="img" aria-label="Portrait of team member" style="background:linear-gradient(180deg,#9d9d9d,#4b4b50)"></div><h3>Daniel Hewett</h3><div class="role">Political Reporter</div><p>Lorem ipsum dolor sit ameteprenim consetetur sadipscing elitr sedes diam nonumy eirmod tempor.</p><div class="socials"><span></span><span></span><span></span><span></span></div></div>
  <div class="member"><div class="img" role="img" aria-label="Portrait of team member" style="background:linear-gradient(180deg,#b4b4b4,#6f6d6b)"></div><h3>Owen Castell</h3><div class="role">Executive Assistance</div><p>Lorem ipsum dolor sit ameteprenim consetetur sadipscing elitr sedes diam nonumy eirmod tempor.</p><div class="socials"><span></span><span></span><span></span><span></span></div></div>
</div>

<h2 class="section-title abs" style="left:259px;top:1591px">Get the Facts</h2>
<div class="accordion">
  <div class="acc-head"><svg width="12" height="10" viewBox="0 0 12 10"><path d="M1 1H9V6H4L1 9Z" fill="#fff"/></svg>Vestibulum pellentesque odio<span class="tog"></span></div>
  <div class="acc-body">
    <p><b>Donec sed odio dui gilla vitae elit libero</b> a pharetra augue. Nullam id dolor id nibh ultricies vehicula ut id elit posuere erat a ante venenatis dapibus posuere</p>
    <p>Nunc nibh eliter feugiat sed congue eu conse ctetur none.Vestibulu necs quam ac diam pharetra mattis ut eget elit. Vestib ulum in pharetra dolor. Aliquam ultrice rutrum libero ut pulv inar lectus tincidunt in. Nunc nibh eliter feugiat sed congue eu conse ctetur none.Vestibulu necs quam.</p>
  </div>
  <div class="acc-item"><span class="ic"></span>Nunc vel justo sitamet metu<span class="tog"></span></div>
  <div class="acc-item"><span class="ic"></span>Mauris bibendum lacus at risus<span class="tog"></span></div>
</div>

<h2 class="section-title abs" style="left:614px;top:1591px">Get Involved</h2>
<div class="tabs-h"><div class="on">Health care</div><div>Immigration</div><div>Volunteer</div></div>
<div class="involved">
  <div class="img" role="img" aria-label="Capitol building under a blue sky"></div>
  <h4>Political acdiam pharetra mattis</h4>
  <p>Nationsla seam ac diam pharetra mattis ut eget elit. Vestib ulum inerse pharetra dolor. Aliquam ultrice rutrum libero ut pulv inar lectus tincidunt inbe. Nunc nibh eliter feugiat sed congue eu conse ctetur none.</p>
</div>

<div class="social-band" role="img" aria-label="Blurred dark city photo"></div>
<div class="social-band row" style="background:none;width:auto;height:auto">
  <span class="soc" style="background:#2aa3dc"></span>
  <span class="soc" style="background:#3b5a98"></span>
  <span class="soc" style="background:#1c7ab5"></span>
  <span class="soc" style="background:#cc2127"></span>
  <span class="soc" style="background:#1d8be6"></span>
  <span class="soc" style="background:#d9482f"></span>
</div>

<footer></footer>
<div class="fcol fnews" style="left:259px">
  <h5>Latest News</h5>
  <ul>
    <li><span class="th" style="background:linear-gradient(#e9b44b,#8fc3ea)"></span><div><b>Platform of the political party</b><small>May 27, 2014 - 3:02 am</small></div></li>
    <li><span class="th" style="background:linear-gradient(#c9404c,#8f9ed1)"></span><div><b>Don't believe the headlines</b><small>May 25, 2014 - 3:03 am</small></div></li>
    <li><span class="th" style="background:linear-gradient(#2c4f86,#e09a4a)"></span><div><b>Restoring America's standing</b><small>May 23, 2014 - 3:03 am</small></div></li>
  </ul>
</div>
<div class="fcol" style="left:436px">
  <h5>Tags</h5>
  <div class="tags"><span>capital</span><span>church</span><span>economy</span><span>education</span><span>election</span><span>ethics</span><span>flag</span><span>funding</span><span>health</span><span>jobs</span><span>national</span><span>politics</span><span>quotes</span><span>relations</span><span>research</span><span>woman</span></div>
</div>
<div class="fcol fcontact" style="left:614px">
  <h5>Contacts</h5>
  <p>Lorem ipsum dolor sit amet, consectetur acing elit. Aenean non urna dolor aecena.</p>
  <ul>
    <li><i></i>318 Harbor Lane, Suite 40,<br>Fairmont 10482.</li>
    <li><i></i>555 014 2270</li>
    <li><i></i>hello@votehallmark.org</li>
  </ul>
</div>
<div class="fcol" style="left:791px">
  <h5>From Gallery</h5>
  <div class="gallery" role="img" aria-label="Grid of small campaign photos">
    <span style="background:#d08a5a"></span><span style="background:#b45a5c"></span><span style="background:#8fb1d8"></span><span style="background:#e0903e"></span>
    <span style="background:#c0874e"></span><span style="background:#e3b9a0"></span><span style="background:#9aa6c6"></span><span style="background:#4f73a6"></span>
  </div>
</div>
<div class="bottombar"></div>
<div class="copyright">Copyright © company name. All rights reserved.</div>
<div class="flinks"><span><i></i>Home</span><span><i></i>Gallery</span><span><i></i>Blog</span><span><i></i>Contact Us</span></div>

</body>
</html>
```